Plumber Referal Program for Water Damage Mitigation

A flyer describing incentives for plumbers to refer us as well as business information. We are called Vorl Restoration and we offer water damage mitigation, mold remediation, and sewage clean up as our 3 services. We are using blue as our company color, here are the following codes included in the logo.

Lighter blue, middle section of logo:
HEX: #2499c7
rgb(36,153,199)
hsl(197,69%,46%)

Darker blue, main color of logo and lettering:
HEX: #1a7da4
rgb(26,125,164)
hsl(197,73%,37%)

Lightest blue, only on small stars at top of logo:
HEX: #9bd3fc
rgb(155,211,252)
hsl(205,94%,80%)

Target Market(s)

Plumbers and other service industries.

Industry/Entity Type

Water Damage Restoration

Requirements
Must have
• Name of our company (Vorl Restoration) along with our number 1(800)555-0192. Website is vorlrestoration.example. 24/7 emergency response. Different methods of payment, including Payquill, Brindo, Coinlet Pay, and written checks. Please include 60-90 minute response time. Please include our 3 services, water damage mitigation, mold remediation, and sewage clean-up. A simple 2 sided flyer.
Nice to have
• Fairly simple design, not too busy. At least 1-2 pictures of water damage and/or mold remediation.
Should not have
• A dollar amount, we would like it to be open ended. Stock photos of smiling people.

```html
<!DOCTYPE html>
<html lang="en">
<head>
<meta charset="utf-8">
<title>Vorl Restoration – Incentives for Plumbers</title>
<link href="https://fonts.googleapis.com/css2?family=Montserrat:ital,wght@0,500;0,600;0,700;0,800;1,700;1,800&display=swap" rel="stylesheet">
<style>
  :root{
    --brand-dark:#1a7da4;
    --brand-mid:#2499c7;
    --brand-light:#9bd3fc;
    --headline-blue:#4cc3f0;
    --navy:#14212b;
    --teal-top:#2b93ba;
    --teal-bottom:#1c7ca3;
    --paper:#ffffff;
    --panel:#f3f4f5;
    --rule:#c9ced2;
    --page-bg:#e6e7e8;
    --ink:#1d2b36;
    --coin-green:#1fb35a;
    --pay-violet:#5b22c9;
  }
  html,body{margin:0;padding:0;width:1200px;height:2235px;overflow:hidden;background:var(--page-bg);}
  .canvas{position:relative;width:1200px;height:2235px;}
  .flyer{position:absolute;left:50px;top:339px;width:1100px;height:1556px;box-shadow:0 14px 36px rgba(0,0,0,.28);background:var(--paper);}
  .flyer svg{display:block;width:100%;height:100%;}
  text{font-family:'Montserrat',sans-serif;}
  .brand-name{font-weight:700;font-size:36px;fill:var(--brand-dark);}
  .headline-top{font-weight:800;font-size:66px;fill:#fff;}
  .headline-bottom{font-weight:800;font-size:66px;fill:var(--headline-blue);}
  .service-label{font-weight:700;font-size:25px;fill:#fff;letter-spacing:.5px;}
  .payment-title{font-weight:700;font-size:29px;fill:var(--brand-dark);letter-spacing:.5px;}
  .payment-name{font-weight:800;font-size:32px;}
  .payment-name.payquill{fill:var(--brand-dark);}
  .payment-name.brindo{fill:var(--pay-violet);}
  .payment-name.coinlet{fill:var(--ink);font-weight:600;font-size:27px;}
  .service-hours{font-weight:800;font-style:italic;font-size:58px;fill:#fff;}
  .service-word{font-weight:700;font-style:italic;font-size:24px;fill:#fff;letter-spacing:1px;}
  .response-title{font-weight:700;font-size:30px;fill:var(--ink);}
  .response-time{font-weight:800;font-size:36px;fill:#fff;}
  .contact-text{font-weight:600;font-size:19px;fill:#fff;}
  .contact-text.phone{font-size:24px;font-weight:700;}
</style>
</head>
<body>
<main class="canvas">
  <article class="flyer">
    <svg viewBox="0 0 1022 1445" xmlns="http://www.w3.org/2000/svg">
      <defs>
        <linearGradient id="photoTone" x1="0" y1="0" x2="1" y2="0">
          <stop offset="0" stop-color="#c9c8c3"/>
          <stop offset=".3" stop-color="#9a8f80"/>
          <stop offset=".55" stop-color="#b9b4ab"/>
          <stop offset=".78" stop-color="#ffffff"/>
        </linearGradient>
        <linearGradient id="tealTone" x1="0" y1="0" x2="0" y2="1">
          <stop offset="0" stop-color="var(--teal-top)"/>
          <stop offset="1" stop-color="var(--teal-bottom)"/>
        </linearGradient>
        <radialGradient id="damageTone"><stop offset="0" stop-color="#b8b6ae"/><stop offset="1" stop-color="#6f6a60"/></radialGradient>
        <radialGradient id="moldTone"><stop offset="0" stop-color="#8c6b45"/><stop offset=".6" stop-color="#cfc6b6"/><stop offset="1" stop-color="#e6e3dc"/></radialGradient>
        <radialGradient id="sewageTone"><stop offset="0" stop-color="#a89a86"/><stop offset="1" stop-color="#5d5243"/></radialGradient>
      </defs>

      <g class="hero-photo" role="img" aria-label="Photo: gloved hand spraying cleaner on a mold-stained wall">
        <rect x="0" y="0" width="1022" height="560" fill="url(#photoTone)"/>
      </g>

      <g class="brand">
        <circle cx="797" cy="108" r="62" fill="var(--brand-mid)"/>
        <text class="brand-name" x="797" y="257" text-anchor="middle" textLength="360" lengthAdjust="spacingAndGlyphs">VORL RESTORATION</text>
      </g>

      <path class="services-field" d="M0,455 Q480,330 1022,360 L1022,1445 L0,1445 Z" fill="url(#tealTone)"/>
      <ellipse class="headline-band" cx="512" cy="535" rx="462" ry="160" fill="var(--navy)"/>

      <text class="headline-top" x="512" y="500" text-anchor="middle">INCENTIVES</text>
      <text class="headline-bottom" x="512" y="572" text-anchor="middle">FOR PLUMBERS</text>

      <g class="service">
        <circle cx="245" cy="708" r="118" fill="var(--brand-mid)"/>
        <circle cx="245" cy="708" r="104" fill="url(#damageTone)" role="img" aria-label="Photo: water-damaged crumbling wall"/>
        <path d="M237,840 h16 l-8,10 z" fill="#fff"/>
        <text class="service-label" x="245" y="880" text-anchor="middle">DAMAGE</text>
        <text class="service-label" x="245" y="912" text-anchor="middle">MITIGATION</text>
      </g>
      <g class="service">
        <circle cx="517" cy="745" r="114" fill="var(--brand-mid)"/>
        <circle cx="517" cy="745" r="100" fill="url(#moldTone)" role="img" aria-label="Photo: mold spreading on a plaster wall"/>
        <path d="M509,873 h16 l-8,10 z" fill="#fff"/>
        <text class="service-label" x="517" y="914" text-anchor="middle">MOLD</text>
        <text class="service-label" x="517" y="946" text-anchor="middle">REMEDIATION</text>
      </g>
      <g class="service">
        <circle cx="778" cy="705" r="118" fill="var(--brand-mid)"/>
        <circle cx="778" cy="705" r="104" fill="url(#sewageTone)" role="img" aria-label="Photo: sewage pipe discharging into murky water"/>
        <path d="M770,840 h16 l-8,10 z" fill="#fff"/>
        <text class="service-label" x="778" y="880" text-anchor="middle">SEWAGE</text>
        <text class="service-label" x="778" y="912" text-anchor="middle">CLEAN UP</text>
      </g>

      <path class="info-panel-edge" d="M0,1152 Q511,796 1022,1152 L1022,1335 L0,1335 Z" fill="var(--rule)"/>
      <path class="info-panel" d="M0,1164 Q511,810 1022,1164 L1022,1335 L0,1335 Z" fill="var(--panel)"/>

      <text class="payment-title" x="511" y="1072" text-anchor="middle">METHODS OF PAYMENT</text>
      <g class="payment-methods">
        <text class="payment-name payquill" x="185" y="1132" textLength="150" lengthAdjust="spacingAndGlyphs">Payquill</text>
        <text class="payment-name brindo" x="360" y="1132" textLength="112" lengthAdjust="spacingAndGlyphs">Brindo</text>
        <rect x="492" y="1104" width="36" height="36" rx="7" fill="var(--coin-green)"/>
        <text class="payment-name coinlet" x="540" y="1131" textLength="160" lengthAdjust="spacingAndGlyphs">Coinlet Pay</text>
        <g class="check-icon" fill="none" stroke="var(--ink)" stroke-width="3">
          <rect x="730" y="1100" width="66" height="40" rx="3" fill="#dcebc6"/>
          <line x1="742" y1="1114" x2="780" y2="1114"/>
          <line x1="742" y1="1124" x2="780" y2="1124"/>
          <line x1="750" y1="1132" x2="784" y2="1132"/>
        </g>
      </g>

      <g class="service-badge">
        <path d="M185,1182 H415 a53,53 0 0 1 0,106 H185 Z" fill="var(--brand-dark)"/>
        <circle cx="185" cy="1235" r="68" fill="var(--brand-mid)"/>
        <circle cx="185" cy="1235" r="55" fill="#fff"/>
        <g stroke="var(--ink)" stroke-width="4" stroke-linecap="round">
          <line x1="185" y1="1235" x2="185" y2="1200"/>
          <line x1="185" y1="1235" x2="165" y2="1235"/>
          <line x1="185" y1="1186" x2="185" y2="1193"/>
          <line x1="185" y1="1277" x2="185" y2="1284"/>
          <line x1="136" y1="1235" x2="143" y2="1235"/>
          <line x1="227" y1="1235" x2="234" y2="1235"/>
        </g>
        <circle cx="185" cy="1235" r="5" fill="var(--ink)"/>
        <text class="service-hours" x="330" y="1245" text-anchor="middle">24/7</text>
        <text class="service-word" x="322" y="1276" text-anchor="middle">SERVICE</text>
      </g>

      <line class="divider" x1="510" y1="1175" x2="510" y2="1305" stroke="var(--ink)" stroke-width="3"/>

      <g class="response">
        <text class="response-title" x="715" y="1210" text-anchor="middle">Our response time</text>
        <rect x="553" y="1222" width="327" height="52" rx="26" fill="var(--brand-dark)" stroke="#fff" stroke-width="3"/>
        <text class="response-time" x="716" y="1261" text-anchor="middle">60-90 MINUTE</text>
      </g>

      <rect class="contact-band" x="0" y="1335" width="1022" height="110" fill="var(--brand-dark)"/>
      <g class="contact-row">
        <circle cx="58" cy="1384" r="15" fill="none" stroke="#fff" stroke-width="3"/>
        <path d="M51,1376 q-2,10 12,16 l3,-4 l-5,-3 l-2,2 q-5,-3 -6,-7 l2,-2 l-3,-5 z" fill="#fff"/>
        <text class="contact-text phone" x="82" y="1393" textLength="184" lengthAdjust="spacingAndGlyphs">1(800)555-0192</text>

        <circle cx="305" cy="1384" r="15" fill="none" stroke="#fff" stroke-width="3"/>
        <g fill="none" stroke="#fff" stroke-width="2">
          <circle cx="305" cy="1384" r="8"/><ellipse cx="305" cy="1384" rx="3.5" ry="8"/><line x1="297" y1="1384" x2="313" y2="1384"/>
        </g>
        <text class="contact-text" x="330" y="1391" textLength="292" lengthAdjust="spacingAndGlyphs">www.vorlrestoration.example</text>

        <circle cx="662" cy="1384" r="15" fill="none" stroke="#fff" stroke-width="3"/>
        <g fill="none" stroke="#fff" stroke-width="2">
          <rect x="653" y="1378" width="18" height="12" rx="1"/><path d="M653,1378 l9,7 l9,-7"/>
        </g>
        <text class="contact-text" x="687" y="1391" textLength="300" lengthAdjust="spacingAndGlyphs">info@vorlrestoration.example</text>
      </g>
    </svg>
  </article>
</main>
</body>
</html>
```